New Business Card Design Project

I need a design for business cards, i am an electrical business called "Tandor Electrical and Communications" i need the cards to be double sided with the company logo on the back (attached) the front needs to say my company name, web site, email address, telephone number, and ABN number and electrical license number. I am open to different arrangements of the information but would like the background to be incorporating something electrical or something that looks smart. open to all additional ideas also.

The company colours are orange and grey see logo attached.

Business Name: Tandor Electrical and Communications
Website: tandorelectricalandcomms.example.au
Email: brent@tandorelectricalandcomms.example.au
Telephone(mobile): 0481203967
ABN: 71829034618
Lic No: 830472F

Target Market(s)

Business entities, Project Managers, Accounts, Clients

Industry/Entity Type

Electrician

Contact Information for Business Card

I need a design for business cards, i am an electrical business called "Tandor Electrical and Communications" i need the cards to be double sided with the company logo on the back (attached) the front needs to say my company name

Font styles to use
Serif
Sans Serif

Colors
f37122
5c5c5c

Requirements
Must have
• Must have the Logo on the back open to different ways of it being on the back but had in mind to keep it central but again open to other options
Nice to have
• A real modern cool background that is eye catching yet contemporary
Should not have
• No backgrounds of a light bulb or plug or anything like that

```html
<!DOCTYPE html>
<html lang="en">
<head>
<meta charset="utf-8">
<title>Tandor Electrical and Communications – Business Card</title>
<link rel="stylesheet" href="https://fonts.googleapis.com/css2?family=Open+Sans:wght@400;600&display=swap">
<style>
  :root {
    --stage: #1f1f1f;
    --card-grey: #5c5c5c;
    --brand-orange: #f37122;
    --white: #ffffff;
    --haze: rgba(215, 215, 215, 0.2);
  }
  * { margin: 0; padding: 0; box-sizing: border-box; }
  html, body { width: 1200px; height: 1200px; overflow: hidden; background: var(--stage); }
  body { font-family: "Open Sans", Arial, sans-serif; position: relative; }

  .card {
    position: absolute; left: 120px; width: 960px; height: 534px;
    background: var(--card-grey); overflow: hidden;
  }
  .card--front { top: 28px; }
  .card--back { top: 598px; }
  .card svg.shapes { position: absolute; inset: 0; }

  .circuit-haze {
    position: absolute;
    background: radial-gradient(ellipse at center, var(--haze) 0%, rgba(215,215,215,0.08) 45%, rgba(215,215,215,0) 72%);
  }

  .front__brand {
    position: absolute; left: 30px; top: 44px;
    color: var(--white); font-weight: 600; font-size: 28px; letter-spacing: 1px; line-height: 1;
  }
  .front__divider { position: absolute; left: 179px; top: 33px; width: 2px; height: 78px; background: #9a9a9a; }
  .front__company {
    position: absolute; left: 222px; top: 46px;
    color: var(--brand-orange); font-size: 34px; font-weight: 400; line-height: 1;
  }
  .contact { position: absolute; left: 220px; top: 150px; list-style: none; }
  .contact li {
    display: flex; align-items: center; height: 56px;
    color: var(--white); font-size: 26px;
  }
  .contact svg { width: 26px; height: 26px; margin-right: 34px; flex: none; }

  .ids { position: absolute; left: 738px; top: 411px; list-style: none; }
  .ids li { display: flex; align-items: center; height: 46px; color: #fde3d2; font-size: 19px; }
  .ids .badge {
    width: 34px; height: 34px; border-radius: 50%; background: #a8531c;
    color: #ffd8bf; font-size: 10px; font-weight: 600; line-height: 11px;
    display: flex; align-items: center; justify-content: center; text-align: center;
    margin-right: 22px;
  }
  .ids .value { width: 120px; text-align: center; }

  .back__logo {
    position: absolute; left: 0; right: 0; top: 185px;
    display: flex; align-items: center; justify-content: center; gap: 28px;
  }
  .back__dot { width: 54px; height: 54px; border-radius: 50%; background: var(--brand-orange); flex: none; }
  .back__name {
    color: var(--white); font-weight: 600; font-size: 120px; letter-spacing: 6px; line-height: 1;
  }
</style>
</head>
<body>

<section class="card card--front" aria-label="Card front">
  <svg class="shapes" width="960" height="534" viewBox="0 0 960 534">
    <path d="M128 534 L230 410 Q262 379 310 379 L960 379 L960 534 Z" fill="var(--brand-orange)"/>
    <path d="M0 429 L102 429 Q128 429 118 452 L82 534 L0 534 Z" fill="var(--white)"/>
  </svg>
  <div class="circuit-haze" role="img" aria-label="Circuit board trace pattern" style="left:-30px;top:140px;width:230px;height:320px;"></div>
  <div class="circuit-haze" role="img" aria-label="Circuit board trace pattern" style="left:880px;top:0;width:110px;height:210px;"></div>

  <div class="front__brand">Tandor</div>
  <div class="front__divider"></div>
  <h1 class="front__company">Tandor Electrical and Communications</h1>

  <ul class="contact">
    <li>
      <svg viewBox="0 0 24 24" aria-hidden="true"><rect x="6" y="2" width="12" height="20" rx="2" fill="none" stroke="#fff" stroke-width="2"/><rect x="9" y="5" width="6" height="4" fill="#fff"/><circle cx="9.5" cy="13" r="1" fill="#fff"/><circle cx="14.5" cy="13" r="1" fill="#fff"/><circle cx="9.5" cy="17" r="1" fill="#fff"/><circle cx="14.5" cy="17" r="1" fill="#fff"/></svg>
      0481203967
    </li>
    <li>
      <svg viewBox="0 0 24 24" aria-hidden="true"><rect x="2" y="5" width="20" height="14" fill="#fff"/><path d="M2 5 L12 13 L22 5" fill="none" stroke="#5c5c5c" stroke-width="2"/></svg>
      brent@tandorelectricalandcomms.example.au
    </li>
    <li>
      <svg viewBox="0 0 24 24" aria-hidden="true"><g fill="none" stroke="#fff" stroke-width="1.8"><circle cx="12" cy="12" r="10"/><ellipse cx="12" cy="12" rx="4.5" ry="10"/><path d="M2 12 H22 M4 7 H20 M4 17 H20"/></g></svg>
      www.tandorelectricalandcomms.example.au
    </li>
  </ul>

  <ul class="ids">
    <li><span class="badge">ABN</span><span class="value">71829034618</span></li>
    <li><span class="badge">Lic<br>No</span><span class="value">830472F</span></li>
  </ul>
</section>

<section class="card card--back" aria-label="Card back">
  <div class="circuit-haze" role="img" aria-label="Circuit board trace pattern" style="left:-40px;top:130px;width:250px;height:270px;"></div>
  <div class="circuit-haze" role="img" aria-label="Circuit board trace pattern" style="left:750px;top:120px;width:250px;height:280px;"></div>
  <div class="back__logo">
    <span class="back__dot" aria-hidden="true"></span>
    <span class="back__name">TANDOR</span>
  </div>
</section>

</body>
</html>
```